Landing Page for a new, High Production, farming technology

Brightfield Yield
We need a single landing page, with an email signup for more information.
We build self-contained, farming boxes out of ISO containers. These containers use hydroponics and LED lighting to provide a year round growing environment for crops. So, you could grow crops anywhere at any time of the year in any environment.
For the purpose of this site, we will be doing split testing between several different themes using different sites and keywords.
This site's focus should be providing our product to people searching for high production farming technology.
We'll be focusing on the following key words: Agriculture, aquaponics, farm, garden, hydroponics, organic food, subsistence farming, urban farming, vertical garden.
Target Market(s)
We are going to be using this page to judge that
Number of Pages Required
1 page
Look and feel
Each slider illustrates characteristics of the customer's brand and the style your logo design should communicate.

```html
<!DOCTYPE html>
<html lang="en">
<head>
<meta charset="utf-8">
<title>Brightfield Yield</title>
<link href="https://fonts.googleapis.com/css2?family=Raleway:wght@400;500;600;700&family=Open+Sans:wght@400;600&display=swap" rel="stylesheet">
<style>
:root{
  --orange:#e08a3c;
  --red:#d8342c;
  --green:#6dbb5c;
  --dark:#1d1d1d;
  --darker:#151515;
  --text:#555;
  --light:#f4f4f4;
  --white:#fff;
}
*{box-sizing:border-box;margin:0;padding:0}
html,body{width:847px;height:1200px;overflow:hidden;background:var(--white)}
body{font-family:"Open Sans",sans-serif;color:var(--text);position:relative}
.site-header{position:absolute;top:0;left:0;width:847px;height:113px;background:var(--white)}
.brand{position:absolute;left:16px;top:12px;width:120px;text-align:center}
.brand-mark{width:34px;height:34px;border-radius:50%;background:var(--orange);margin:0 auto 8px}
.brand-name{font-family:"Raleway",sans-serif;font-weight:600;font-size:12px;letter-spacing:2px;color:var(--green);line-height:1.25}
.top-bar{position:absolute;right:40px;top:28px;display:flex;align-items:center;gap:12px;font-size:13px;color:#333}
.top-bar .phone{display:flex;align-items:center;gap:5px}
.search{width:110px;height:22px;border:1px solid #ccc;border-radius:3px;font-size:10px;color:#999;padding:3px 7px;position:relative}
.search svg{position:absolute;right:5px;top:4px}
.main-nav{position:absolute;right:30px;top:68px;display:flex;gap:28px;font-size:13px;font-family:"Raleway",sans-serif;font-weight:500;color:#333}
.main-nav .active{color:var(--orange)}
.hero{position:absolute;top:113px;left:0;width:847px;height:437px;background:linear-gradient(120deg,#8f9e92 0%,#c7cec4 30%,#7ea05e 60%,#3d6a2a 85%,#27461b 100%)}
.hero-title{position:absolute;left:79px;top:262px;font-family:"Raleway",sans-serif;font-weight:500;font-size:46px;color:var(--red)}
.hero-sub{position:absolute;left:79px;top:318px;font-family:"Raleway",sans-serif;font-weight:600;font-size:22px;color:var(--white)}
.hero-dots{position:absolute;right:28px;top:272px;display:flex;flex-direction:column;gap:5px}
.hero-dots span{width:7px;height:7px;border-radius:50%;background:rgba(255,255,255,.6)}
.hero-dots .on{background:var(--red)}
.features{position:absolute;top:465px;left:62px;display:flex;gap:0}
.feature{width:175px;height:190px;position:relative;text-align:center}
.feature-photo{position:absolute;inset:40px 0 0 0}
.f1 .feature-photo{background:linear-gradient(160deg,#5f7a3f,#2f4a22)}
.f2 .feature-photo{background:linear-gradient(160deg,#e9a160,#c96a26)}
.f3 .feature-photo{background:linear-gradient(160deg,#4d6e3a,#243b1c)}
.f4 .feature-photo{background:linear-gradient(160deg,#6b8a4d,#34512a)}
.feature-icon{position:absolute;left:50%;top:0;transform:translateX(-50%);width:70px;height:70px;border-radius:50%;background:var(--white);display:flex;align-items:center;justify-content:center;box-shadow:0 1px 4px rgba(0,0,0,.2)}
.feature-label{position:absolute;left:0;right:0;top:102px;font-family:"Raleway",sans-serif;font-weight:600;font-size:22px;color:var(--white)}
.feature-go{position:absolute;left:50%;bottom:-8px;transform:translateX(-50%);width:22px;height:22px;border-radius:50%;background:#333;display:flex;align-items:center;justify-content:center}
.f2 .feature-go{background:var(--orange)}
.welcome{position:absolute;top:695px;left:0;width:847px;text-align:center}
.welcome h1{font-family:"Raleway",sans-serif;font-weight:500;font-size:32px;color:#333}
.welcome p{width:730px;margin:20px auto 0;font-size:11.5px;line-height:1.75;color:#777}
.btn-more{display:inline-block;margin-top:26px;width:142px;height:38px;line-height:38px;background:var(--green);color:var(--white);font-size:14px;font-family:"Raleway",sans-serif;font-weight:600}
.site-footer{position:absolute;top:936px;left:0;width:847px;height:264px;background:var(--dark);border-top:10px solid var(--orange)}
.foot-col{position:absolute;top:60px;color:#ddd;font-size:10.5px}
.foot-col h3{font-family:"Raleway",sans-serif;font-weight:600;font-size:13px;color:var(--white);margin-bottom:18px;text-transform:uppercase;letter-spacing:.5px}
.col-info{left:84px}
.col-info li{list-style:none;margin-bottom:9px}
.col-info li::before{content:"›";margin-right:7px;color:var(--orange)}
.col-contact{left:287px;width:210px}
.contact-row{display:flex;gap:10px;margin-bottom:12px;line-height:1.45}
.contact-row svg{flex:0 0 auto;margin-top:2px}
.col-mail{left:592px;width:200px}
.col-mail p{line-height:1.5;margin-bottom:14px}
.mail-form{display:flex;align-items:center;width:178px;height:26px;border:1px solid #777;border-radius:14px;padding:0 4px 0 12px;color:#999;font-size:10px;justify-content:space-between}
.mail-form span.go{width:18px;height:18px;border-radius:50%;background:var(--orange);display:flex;align-items:center;justify-content:center}
.copyright{position:absolute;left:0;bottom:0;width:847px;height:56px;border-top:1px solid #444;background:var(--darker);text-align:center;line-height:56px;font-size:10px;color:#bbb}
.lang{position:absolute;right:24px;bottom:18px;font-size:10px;color:#bbb}
</style>
</head>
<body>
<header class="site-header">
  <div class="brand">
    <div class="brand-mark"></div>
    <div class="brand-name">BRIGHTFIELD<br>YIELD</div>
  </div>
  <div class="top-bar">
    <span class="phone"><svg width="12" height="12" viewBox="0 0 24 24"><path d="M6.6 10.8a15 15 0 0 0 6.6 6.6l2.2-2.2c.3-.3.7-.4 1-.2 1.1.4 2.3.6 3.6.6.6 0 1 .4 1 1V20c0 .6-.4 1-1 1A17 17 0 0 1 3 4c0-.6.4-1 1-1h3.5c.6 0 1 .4 1 1 0 1.3.2 2.5.6 3.6.1.3 0 .7-.2 1z" fill="#e08a3c"/></svg>0865550142</span>
    <div class="search">Search<svg width="11" height="11" viewBox="0 0 24 24"><circle cx="10" cy="10" r="7" stroke="#555" stroke-width="2.5" fill="none"/><path d="M15 15l6 6" stroke="#555" stroke-width="2.5"/></svg></div>
  </div>
  <nav class="main-nav">
    <span class="active">Home</span><span>About us</span><span>Services</span><span>Products</span><span>Blog</span><span>Contact Us</span>
  </nav>
</header>

<section class="hero" role="img" aria-label="Strawberries growing inside a bright greenhouse">
  <h2 class="hero-title">Brightfield Yield</h2>
  <p class="hero-sub">Farming boxes out of ISO containers</p>
  <div class="hero-dots"><span></span><span class="on"></span><span></span></div>
</section>

<section class="features">
  <div class="feature f1">
    <div class="feature-photo" role="img" aria-label="Seedlings in a growing tray"></div>
    <div class="feature-icon"><svg width="34" height="34" viewBox="0 0 24 24"><circle cx="12" cy="12" r="4" fill="none" stroke="#333" stroke-width="2"/><path d="M12 2v4M12 18v4M2 12h4M18 12h4M5 5l3 3M16 16l3 3M5 19l3-3M16 8l3-3" stroke="#333" stroke-width="2"/></svg></div>
    <div class="feature-label">Services</div>
    <div class="feature-go"><svg width="10" height="10" viewBox="0 0 10 10"><path d="M3 1l4 4-4 4" stroke="#fff" stroke-width="1.6" fill="none"/></svg></div>
  </div>
  <div class="feature f2">
    <div class="feature-photo" role="img" aria-label="Hands holding young plants"></div>
    <div class="feature-icon"><svg width="34" height="34" viewBox="0 0 24 24"><path d="M12 21V10M12 12c-4 0-6-3-6-6 3 0 6 2 6 6zM12 14c4 0 6-3 6-6-3 0-6 2-6 6z" stroke="#e08a3c" stroke-width="2" fill="none"/></svg></div>
    <div class="feature-label">Products</div>
    <div class="feature-go"><svg width="10" height="10" viewBox="0 0 10 10"><path d="M3 1l4 4-4 4" stroke="#fff" stroke-width="1.6" fill="none"/></svg></div>
  </div>
  <div class="feature f3">
    <div class="feature-photo" role="img" aria-label="Rows of leafy crops"></div>
    <div class="feature-icon"><svg width="34" height="34" viewBox="0 0 24 24"><path d="M4 20h16M6 20V12M12 20V7M18 20v-5" stroke="#333" stroke-width="2.5"/></svg></div>
    <div class="feature-label">Solutions</div>
    <div class="feature-go"><svg width="10" height="10" viewBox="0 0 10 10"><path d="M3 1l4 4-4 4" stroke="#fff" stroke-width="1.6" fill="none"/></svg></div>
  </div>
  <div class="feature f4">
    <div class="feature-photo" role="img" aria-label="Hydroponic growing channels"></div>
    <div class="feature-icon"><svg width="34" height="34" viewBox="0 0 24 24"><path d="M12 3c3 4 6 8 6 11a6 6 0 0 1-12 0c0-3 3-7 6-11z" stroke="#333" stroke-width="2" fill="none"/></svg></div>
    <div class="feature-label">Hydroponics</div>
    <div class="feature-go"><svg width="10" height="10" viewBox="0 0 10 10"><path d="M3 1l4 4-4 4" stroke="#fff" stroke-width="1.6" fill="none"/></svg></div>
  </div>
</section>

<section class="welcome">
  <h1>Welcome to Brightfield Yield</h1>
  <p>The point of using Lorem Ipsum is that it has a more-or-less normal distribution of letters, as opposed to using 'Content here, content here', making it look like readable English. Many desktop publishing packages and web page editors now use Lorem Ipsum as their default model text, and a search for 'lorem ipsum' will uncover many web sites still in their infancy.</p>
  <a class="btn-more">View More ›</a>
</section>

<footer class="site-footer">
  <div class="foot-col col-info">
    <h3>Information</h3>
    <ul><li>Privacy Policy</li><li>Your Account</li><li>Advanced Search</li><li>Contact Us</li></ul>
  </div>
  <div class="foot-col col-contact">
    <h3>Contact Us</h3>
    <div class="contact-row"><svg width="11" height="13" viewBox="0 0 24 28"><path d="M12 1a9 9 0 0 0-9 9c0 7 9 17 9 17s9-10 9-17a9 9 0 0 0-9-9z" fill="#fff"/><circle cx="12" cy="10" r="3.5" fill="#1d1d1d"/></svg><span>12 Orchard Business Park, Mill Road<br>Fenwick FN4 2LD</span></div>
    <div class="contact-row"><svg width="11" height="11" viewBox="0 0 24 24"><path d="M6.6 10.8a15 15 0 0 0 6.6 6.6l2.2-2.2c.3-.3.7-.4 1-.2 1.1.4 2.3.6 3.6.6.6 0 1 .4 1 1V20c0 .6-.4 1-1 1A17 17 0 0 1 3 4c0-.6.4-1 1-1h3.5c.6 0 1 .4 1 1 0 1.3.2 2.5.6 3.6.1.3 0 .7-.2 1z" fill="#fff"/></svg><span>01632 960418</span></div>
    <div class="contact-row"><svg width="12" height="10" viewBox="0 0 24 18"><rect x="1" y="1" width="22" height="16" fill="none" stroke="#fff" stroke-width="2"/><path d="M1 1l11 9 11-9" stroke="#fff" stroke-width="2" fill="none"/></svg><span>info@brightfieldyield.com</span></div>
  </div>
  <div class="foot-col col-mail">
    <h3>Join our mailing list</h3>
    <p>Sign up for news and updates about our farms.</p>
    <div class="mail-form">Email address<span class="go"><svg width="8" height="8" viewBox="0 0 10 10"><path d="M3 1l4 4-4 4" stroke="#fff" stroke-width="1.8" fill="none"/></svg></span></div>
  </div>
  <div class="copyright">Copyright © 2016. All Rights Reserved</div>
  <div class="lang">EN</div>
</footer>
</body>
</html>
```